Powerpoint presentation sales pack for ground transfer company

Need a base pack for sales presentation for KVT,
We specialise in corporate ground transport (similar to ZOLTA)
Needs to be sharp and have a modern feel
Looking for a good master slide design and page layout for provide content
Check out our website https://kvt.example/
Check out our competitors https://www.zolta.example/business https://www.hollisterlimorun.example.au
Look at other marketing material available and old draft powerpoint pack for content and design ideas

```html
<!DOCTYPE html>
<html lang="en">
<head>
<meta charset="utf-8">
<title>The KVT Difference</title>
<link rel="stylesheet" href="https://fonts.googleapis.com/css2?family=Open+Sans:wght@400;600;700&display=swap">
<style>
  :root {
    --teal: #3bb9a3;
    --teal-star: #5cc1b2;
    --charcoal: #2b2b2b;
    --title-grey: #565656;
    --text-light: #f2f2f2;
    --white: #ffffff;
  }
  * { margin: 0; padding: 0; box-sizing: border-box; }
  html, body { width: 1200px; height: 900px; overflow: hidden; background: var(--white); }
  body { font-family: "Open Sans", Arial, sans-serif; }
  .slide { position: relative; width: 1200px; height: 900px; background: var(--white); overflow: hidden; }
  .accent-tab { position: absolute; left: 63px; top: 0; width: 175px; height: 70px; background: var(--teal); }
  .slide-title {
    position: absolute; left: 60px; top: 92px;
    font-size: 60px; font-weight: 700; letter-spacing: -0.5px; line-height: 1;
    color: var(--title-grey);
  }
  .slide-title .brand { color: var(--teal); }
  .content-band { position: absolute; left: 0; top: 200px; width: 1200px; height: 650px; background: var(--charcoal); }
  .feature-panel { position: absolute; left: 63px; top: 200px; width: 399px; height: 650px; background: var(--white); }
  .rating { position: absolute; left: 80px; top: 36px; }
  .agent-photo {
    position: absolute; left: 4px; top: 133px; width: 395px; height: 517px;
    background: linear-gradient(160deg, #e9ecef 0%, #d8cfc7 45%, #8a7366 70%, #3a3432 100%);
  }
  .benefits { position: absolute; left: 505px; top: 245px; width: 640px; list-style: none; }
  .benefits li {
    position: relative; padding-left: 42px; margin-bottom: 13px;
    font-size: 30px; line-height: 1.45; color: var(--text-light);
  }
  .benefits li::before {
    content: ""; position: absolute; left: 0; top: 17px;
    width: 11px; height: 11px; background: var(--teal);
  }
  .page-number { position: absolute; left: 1022px; top: 858px; font-size: 16px; color: var(--teal); }
  .page-rule { position: absolute; left: 967px; top: 891px; width: 146px; height: 9px; background: var(--teal); }
</style>
</head>
<body>
<main class="slide">
  <div class="accent-tab"></div>
  <h1 class="slide-title"><span class="brand">KVT</span> Difference</h1>
  <h1 class="slide-title" style="visibility:hidden" aria-hidden="true"></h1>

  <div class="content-band"></div>

  <section class="feature-panel">
    <svg class="rating" width="240" height="44" viewBox="0 0 240 44" aria-label="Five star rating">
      <defs>
        <polygon id="star" points="20,2 25,15.5 39.5,15.5 28,24.5 32,39 20,30.5 8,39 12,24.5 0.5,15.5 15,15.5" fill="#5cc1b2"/>
      </defs>
      <use href="#star" x="0"/>
      <use href="#star" x="48"/>
      <use href="#star" x="96"/>
      <use href="#star" x="144"/>
      <use href="#star" x="192"/>
    </svg>
    <div class="agent-photo" role="img" aria-label="Photo of a smiling customer service agent wearing a headset, with colleagues at a call centre behind her"></div>
  </section>

  <ul class="benefits">
    <li>Technology driven business</li>
    <li>On Time - Guarantee</li>
    <li>Fixed, All Inclusive Pricing</li>
    <li>360 Degree Feedback</li>
    <li>Preferred Drivers by city by traveller</li>
    <li>Driver&nbsp; Contact Information provided on booking</li>
    <li>Reconfirmation 4 hours prior to all bookings</li>
    <li>Pre Trip Driver Safety Declarations</li>
  </ul>

  <div class="page-number">Page 5</div>
  <div class="page-rule"></div>
</main>
</body>
</html>
```